Recital Flyer - Step Into Starlight

I need a flyer to depict a contemporary recital theme, "Step Into Starlight..." for my 6th Annual Recital. I am looking for a Velmont Plaza "look" that is set in Detroit or has a "Detroit" Influence.

Here are some of the featured plays we are using: Ghost in the Ballroom, Glitterbug, A Kettle Waltz, The Otter Queen, The Tinted Meadow, Slipper Bash, Tamberly, Kick Up Tha Beat/Kick Up Tha Soul, Rivetline The Revue, Tapworth, Glint and more!
Updates

hi there I would like to add a $75 tip, how do I do that?

Target Market(s)

Dancers - students ages 3-15

Industry/Entity Type

Dance Studio

Font styles to use
Other font styles liked:
• Broadway or something familiar

Requirements
Must have
• My Logo and pertinent information on it:
• Date: June 24, 2017
• Time: 2 PM & 7 PM
• Location: Pinecrest Hollow High School
• 418 Marlow Rd, Commerce Charter Twp, MI 48390
Nice to have
• A New York (Velmont Plaza) flair with a gritty Detroit Influnce!

```html
<!DOCTYPE html>
<html lang="en">
<head>
<meta charset="utf-8">
<title>Step Into Starlight – 6th Annual Recital</title>
<link rel="stylesheet" href="https://fonts.googleapis.com/css2?family=Cinzel:wght@700&family=Great+Vibes&display=swap">
<style>
  :root {
    --navy: #0d1a45;
    --navy-deep: #070f2e;
    --red: #c3161f;
    --red-dark: #6a080c;
    --gold: #d9a53a;
    --gold-light: #f4dc7a;
    --gold-deep: #a9700f;
    --white: #ffffff;
    --ink: #1b0e0e;
  }
  * { margin: 0; padding: 0; box-sizing: border-box; }
  html, body { width: 902px; height: 1200px; overflow: hidden; background: var(--white); }
  .flyer { position: relative; width: 902px; height: 1200px; overflow: hidden; font-family: "Cinzel", "Times New Roman", serif; font-weight: 700; color: var(--white); }
  .flyer-backdrop { position: absolute; inset: 0; }
  .seal { position: absolute; left: 488px; top: 34px; width: 240px; height: 240px; }
  .seal-shape { position: absolute; inset: 0; }
  .seal-number { position: absolute; left: 0; right: 0; top: 62px; text-align: center; font-family: "Great Vibes", cursive; font-weight: 400; font-size: 84px; line-height: 1; }
  .seal-caption { position: absolute; left: 0; right: 0; top: 150px; text-align: center; font-family: "Great Vibes", cursive; font-weight: 400; font-size: 30px; line-height: 1; }
  .headline { position: absolute; top: 588px; left: 0; right: 0; text-align: center; font-size: 42px; font-weight: 700; letter-spacing: 1px; text-shadow: 0 2px 3px rgba(0,0,0,.4); }
  .date-pill { position: absolute; left: 161px; top: 662px; width: 580px; height: 78px; border-radius: 22px; background: var(--navy-deep); border: 2px solid #c9c9d8; display: flex; align-items: center; justify-content: center; font-size: 50px; font-weight: 700; box-shadow: 0 10px 14px rgba(0,0,0,.35); }
  .time-pill { position: absolute; left: 234px; top: 774px; width: 432px; height: 46px; border-radius: 12px; background: linear-gradient(#a20d14, var(--red-dark)); border: 2px solid #e8c8c8; display: flex; align-items: center; justify-content: center; font-size: 26px; font-weight: 700; box-shadow: 0 4px 8px rgba(0,0,0,.45); }
  .location { position: absolute; top: 843px; left: 0; right: 0; text-align: center; font-size: 22px; font-weight: 700; }
  .location-venue { color: var(--gold-light); }
  .address { position: absolute; top: 894px; left: 0; right: 0; text-align: center; font-size: 17px; font-weight: 700; }
  .studio-mark { position: absolute; left: 276px; top: 946px; width: 350px; height: 212px; border-radius: 50%; background: var(--white); border: 5px solid var(--gold); box-shadow: 0 0 0 2px var(--gold-deep); display: flex; flex-direction: column; align-items: center; justify-content: center; gap: 10px; text-align: center; }
  .studio-mark-square { width: 30px; height: 30px; background: var(--red-dark); }
  .studio-mark-name { font-size: 24px; font-weight: 700; line-height: 1.2; color: var(--red-dark); }
</style>
</head>
<body>
<main class="flyer">
  <svg class="flyer-backdrop" width="902" height="1200" viewBox="0 0 902 1200">
    <defs>
      <radialGradient id="redField" cx="50%" cy="55%" r="65%">
        <stop offset="0" stop-color="#d01c25"/>
        <stop offset="0.6" stop-color="#a30f17"/>
        <stop offset="1" stop-color="#5e070b"/>
      </radialGradient>
      <linearGradient id="goldBand" x1="0" y1="0" x2="0" y2="1">
        <stop offset="0" stop-color="#a9700f"/>
        <stop offset="0.5" stop-color="#e9c458"/>
        <stop offset="0.8" stop-color="#f6e27e"/>
        <stop offset="1" stop-color="#c08a1a"/>
      </linearGradient>
      <linearGradient id="goldSwoosh" x1="0" y1="0" x2="1" y2="0">
        <stop offset="0" stop-color="#b5821c"/>
        <stop offset="0.6" stop-color="#f1d36a"/>
        <stop offset="1" stop-color="#c99528"/>
      </linearGradient>
      <linearGradient id="nightTower" x1="0" y1="0" x2="0" y2="1">
        <stop offset="0" stop-color="#2a2f6b"/>
        <stop offset="0.55" stop-color="#54407a"/>
        <stop offset="1" stop-color="#c98a3a"/>
      </linearGradient>
    </defs>
    <rect class="night-sky" width="902" height="1200" fill="var(--navy)"/>
    <rect class="tower-photo" x="0" y="30" width="490" height="560" fill="url(#nightTower)" role="img" aria-label="Photo of an illuminated clock tower at night"/>
    <path class="swoosh-gold" d="M0 538 Q470 500 902 196 L902 240 Q470 540 0 566 Z" fill="url(#goldSwoosh)"/>
    <path class="swoosh-white" d="M0 552 Q470 518 902 222 L902 236 Q470 534 0 560 Z" fill="var(--white)"/>
    <path class="red-field" d="M0 562 Q470 538 902 238 L902 1200 L0 1200 Z" fill="url(#redField)"/>
    <path class="band-white" d="M0 976 Q451 1010 902 970 L902 996 Q451 1036 0 1000 Z" fill="var(--white)"/>
    <path class="band-gold" d="M0 998 Q451 1034 902 994 L902 1200 L0 1200 Z" fill="url(#goldBand)"/>
  </svg>

  <div class="seal">
    <svg class="seal-shape" width="240" height="240" viewBox="0 0 240 240" role="img" aria-label="Gold anniversary seal with ribbon">
      <circle cx="120" cy="120" r="112" fill="var(--ink)" stroke="var(--gold)" stroke-width="10"/>
    </svg>
    <div class="seal-number">6th</div>
    <div class="seal-caption">Annual Recital</div>
  </div>

  <h1 class="headline">STEP INTO STARLIGHT...</h1>
  <div class="date-pill">JUNE 24, 2017</div>
  <div class="time-pill">TIME: 2 PM &amp; 7 PM</div>
  <p class="location">LOCATION: <span class="location-venue">PINECREST HOLLOW HIGH SCHOOL</span></p>
  <p class="address">418 MARLOW RD, COMMERCE CHARTER TWP, MI 48390</p>

  <div class="studio-mark">
    <span class="studio-mark-square"></span>
    <span class="studio-mark-name">HARBOR LANE<br>DANCE STUDIO LLC</span>
  </div>
</main>
</body>
</html>
```